Hair extension stockists

We need a logo and a packaging design, to show our range of hair extensions. We ideally want cream or black with an elegant feel. We would like a box that has a see through small element so that customers can see what colour is inside and we also want the box to open up from the side. Our name is Velmora Hair.This is for our standard range, in the next few months we will also have a luxury range. We are open to all ideas as we want to stand out from the rest.

Industry/Entity Type
Graphic Design

```html
<!DOCTYPE html>
<html lang="en">
<head>
<meta charset="UTF-8">
<title>Velmora Hair – Clip In Extensions Pack</title>
<link href="https://fonts.googleapis.com/css2?family=Great+Vibes&family=Delius&display=swap" rel="stylesheet">
<style>
  :root {
    --cream: #fbf8d2;
    --charcoal: #2b2a2a;
    --ink: #3a3838;
    --rose: #e9507a;
    --white: #ffffff;
    --hair-dark: #3b2a1c;
    --hair-mid: #6b4f33;
    --hair-light: #a88656;
  }
  * { margin: 0; padding: 0; box-sizing: border-box; }
  html, body {
    width: 1200px;
    height: 2400px;
    overflow: hidden;
    background: var(--cream);
  }
  .pack {
    position: relative;
    width: 1200px;
    height: 2400px;
    background: var(--cream);
    overflow: hidden;
    font-family: "Delius", "Comic Sans MS", sans-serif;
    color: var(--ink);
  }
  .top-band {
    position: absolute;
    left: 0; top: 0;
    width: 1200px; height: 80px;
    background: var(--charcoal);
  }
  .brand {
    position: absolute;
    left: 0; top: 150px;
    width: 1200px;
    display: flex;
    align-items: center;
    justify-content: center;
    gap: 36px;
  }
  .brand-name {
    font-family: "Great Vibes", cursive;
    font-size: 200px;
    line-height: 1;
    color: var(--ink);
    font-weight: 400;
  }
  .brand-dot {
    width: 70px; height: 70px;
    border-radius: 50%;
    background: var(--rose);
  }
  .tagline {
    position: absolute;
    left: 0; top: 590px;
    width: 1200px;
    text-align: center;
    font-size: 64px;
    color: var(--ink);
  }
  .spec-band {
    position: absolute;
    left: 0; top: 800px;
    width: 1200px; height: 440px;
    background: var(--rose);
  }
  .spec-list {
    position: absolute;
    left: 36px; top: 840px;
    list-style: none;
    color: var(--white);
    font-size: 54px;
    line-height: 98px;
  }
  .coverage {
    position: absolute;
    left: 140px; top: 1270px;
    font-size: 60px;
    color: var(--ink);
  }
  .shade-window {
    position: absolute;
    left: 516px; top: 736px;
    width: 640px; height: 1184px;
    border-radius: 50%;
    border: 4px solid var(--charcoal);
    background:
      linear-gradient(100deg,
        var(--hair-dark) 0%,
        var(--hair-mid) 22%,
        var(--hair-dark) 38%,
        var(--hair-light) 55%,
        var(--hair-mid) 70%,
        var(--hair-light) 85%,
        var(--hair-mid) 100%);
  }
  .floral-area {
    position: absolute;
    left: 0; top: 1620px;
    width: 620px; height: 780px;
    background: radial-gradient(ellipse at 40% 60%, rgba(60,58,58,0.22) 0%, rgba(60,58,58,0.08) 55%, rgba(60,58,58,0) 80%);
  }
</style>
</head>
<body>
  <main class="pack">
    <div class="top-band"></div>

    <header class="brand">
      <span class="brand-name">Velmora Hair</span>
      <span class="brand-dot"></span>
    </header>

    <p class="tagline">100% Remy Human hair</p>

    <div class="spec-band"></div>
    <ul class="spec-list">
      <li>Colour : #P4/27</li>
      <li>Dark Brown/</li>
      <li>Caramel Blonde</li>
      <li>20" Clip In</li>
    </ul>

    <p class="coverage">Full Head</p>

    <div class="shade-window" role="img" aria-label="Oval see-through window showing dark brown hair with caramel blonde highlights"></div>

    <div class="floral-area" role="img" aria-label="Decorative dark grey floral vine ornament"></div>
  </main>
</body>
</html>
```